I need a business card design for a new company that will be doing consulting work around issues of cultural competency, and diversity and inclusion. I would like the design to be crisp and clear with bold but conservative colors and incorporate shades of blue

Target Market(s)

Small businesses, schools, non-profits

Industry/Entity Type

Consulting

Font styles to use
Serif
Sans Serif

Colors
0c5ba6
6b449b
3276b5
0292cd

Requirements
Must have
• A Morrow Venture (name of company)
• Lemlem Tavish
• CEO
• lemlem@amorrowventure.com
• (215)483-2756

```html
<!DOCTYPE html>
<html lang="en">
<head>
<meta charset="utf-8">
<title>Lemlem Tavish – Business Card</title>
<link rel="stylesheet" href="https://fonts.googleapis.com/css2?family=Outfit:wght@300;600&display=swap">
<style>
  :root {
    --brand-blue: #135ea9;
    --text-blue: #2a5aa7;
    --accent-yellow: #f2e600;
    --card-white: #ffffff;
    --edge-grey: #e6e2d6;
  }
  html, body {
    margin: 0;
    padding: 0;
    width: 1200px;
    height: 685px;
    overflow: hidden;
    background: var(--card-white);
  }
  .card {
    position: relative;
    width: 1200px;
    height: 685px;
    background: var(--card-white);
    box-shadow: inset 1px 0 0 var(--edge-grey);
    font-family: "Outfit", sans-serif;
    overflow: hidden;
  }
  .card__header {
    position: absolute;
    inset: 0;
    width: 1200px;
    height: 685px;
  }
  .card__line {
    position: absolute;
    left: 0;
    width: 100%;
    margin: 0;
    text-align: center;
    line-height: 1;
    white-space: nowrap;
  }
  .card__name {
    top: 118px;
    color: var(--card-white);
    font-weight: 600;
    font-size: 80px;
    letter-spacing: -0.5px;
  }
  .card__title {
    top: 222px;
    color: var(--card-white);
    font-weight: 300;
    font-size: 40px;
  }
  .card__contact {
    color: var(--text-blue);
    font-weight: 300;
    font-size: 39px;
  }
  .card__email { top: 464px; }
  .card__phone { top: 541px; }
  .card__company {
    top: 622px;
    color: var(--text-blue);
    font-weight: 600;
    font-size: 24px;
    letter-spacing: 1px;
  }
</style>
</head>
<body>
  <div class="card">
    <svg class="card__header" viewBox="0 0 1200 685" aria-hidden="true">
      <polygon points="0,0 1200,0 1200,232 600,421 0,232" fill="var(--brand-blue)"/>
      <polyline points="0,232 600,421 1200,232" fill="none" stroke="var(--accent-yellow)" stroke-width="7"/>
    </svg>
    <h1 class="card__line card__name">Lemlem Tavish</h1>
    <p class="card__line card__title">CEO</p>
    <p class="card__line card__contact card__email">lemlem@amorrowventure.com</p>
    <p class="card__line card__contact card__phone">(215)483-2756</p>
    <p class="card__line card__company">A Morrow Venture</p>
  </div>
</body>
</html>
```